Ironfield Grillhouse

We are changing our restaurant from a casual upmarket dining restaurant, to an upmarket steakhouse. The restaurant is located at Ironfield Lodge, Silver Pine Summit Resort, BC, Canada.

The A - frame Signs are 3 feet wide by 5 foot high.
Must also work as a poster size.

Target Market(s)

25 to 65's skiers, families, affluent home owners.

Industry/Entity Type

Restaurant

Colors

Designer to choose colors to be used in the design.

Requirements
Must have
• A big, juicy, flame grilled steak image.
• Located at Ironfield lodge.
Nice to have
• Must be bold and enticing, need to convince the tired skiers that they just have to have an awesome steak for dinner.
• Should be simple, straight to the point.
• People drinking, dining, having a great dining experience.
Should not have
• bright colors

```html
<!DOCTYPE html>
<html lang="en">
<head>
<meta charset="utf-8">
<title>Ironfield Grillhouse — A-frame Poster</title>
<link href="https://fonts.googleapis.com/css2?family=Abril+Fatface&family=Cinzel:wght@400&family=Playfair+Display:wght@600&family=Russo+One&display=swap" rel="stylesheet">
<style>
  :root {
    --page: #000000;
    --ember-deep: #2a0a05;
    --ember-mid: #7a2a10;
    --ember-hot: #c9601c;
    --smoke: rgba(0, 0, 0, 0.72);
    --maroon-veil: rgba(70, 14, 10, 0.78);
    --gold: #e8ad22;
    --white: #ffffff;
  }
  * { margin: 0; padding: 0; box-sizing: border-box; }
  html, body {
    width: 999px; height: 1200px; overflow: hidden;
    background: var(--page);
  }
  .poster {
    position: absolute; left: 97px; top: 32px;
    width: 806px; height: 1136px; overflow: hidden;
  }
  .grill-backdrop {
    position: absolute; inset: 0;
    background:
      radial-gradient(ellipse 260px 200px at 740px 640px, #8a4a22 0%, transparent 70%),
      radial-gradient(ellipse 220px 180px at 60px 860px, #b0501a 0%, transparent 70%),
      radial-gradient(ellipse 300px 160px at 200px 30px, #c4661e 0%, transparent 70%),
      radial-gradient(ellipse 200px 160px at 760px 1080px, #d06a1c 0%, transparent 70%),
      linear-gradient(160deg, var(--ember-mid) 0%, var(--ember-deep) 45%, #5a200c 70%, var(--ember-deep) 100%);
  }
  .shade { position: absolute; inset: 0; }
  .photo {
    position: absolute;
  }
  .photo--dining-room {
    left: 0; top: 51px; width: 398px; height: 297px;
    clip-path: polygon(0 0, 100% 0, 75% 100%, 0 100%);
    background: linear-gradient(180deg, #6b4a30 0%, #3a2a22 45%, #2a2420 100%);
  }
  .photo--toast {
    left: 415px; top: 786px; width: 391px; height: 298px;
    clip-path: polygon(12% 0, 100% 0, 100% 100%, 0 100%);
    background: linear-gradient(120deg, #4a2230 0%, #8a3a3a 40%, #3a3a5a 75%, #1e2a4a 100%);
  }
  .brand {
    position: absolute; left: 405px; top: 112px; width: 316px;
    text-align: center; color: var(--white);
    font-family: "Cinzel", serif; font-weight: 400;
    font-size: 33px; line-height: 36px; letter-spacing: 0.5px;
  }
  .headline-veil {
    position: absolute; left: 0; top: 390px; width: 660px; height: 356px;
    clip-path: polygon(0 0, 100% 0, 88% 100%, 0 100%);
    background: var(--maroon-veil);
  }
  .gold-bar {
    position: absolute; left: 0; height: 24px; background: var(--gold);
  }
  .gold-bar--top { top: 366px; width: 731px; clip-path: polygon(0 0, 100% 0, 98.4% 100%, 0 100%); }
  .gold-bar--bottom { top: 746px; width: 589px; height: 22px; clip-path: polygon(0 0, 100% 0, 98.3% 100%, 0 100%); }
  .headline { position: absolute; left: 0; width: 100%; }
  .headline__line {
    position: absolute; left: 39px; color: var(--white);
    font-family: "Russo One", sans-serif; font-size: 50px; line-height: 1;
    letter-spacing: 1.5px; white-space: nowrap;
  }
  .headline__line--lead { top: 438px; }
  .headline__line--close { top: 646px; letter-spacing: 2.4px; }
  .headline__accent {
    position: absolute; left: 30px; top: 488px; color: var(--gold);
    font-family: "Abril Fatface", serif; font-size: 138px; line-height: 1;
    letter-spacing: -2px; white-space: nowrap;
    transform: scaleX(0.9); transform-origin: left top;
  }
  .tagline {
    position: absolute; left: 40px; width: 392px; text-align: center;
    color: var(--white); font-family: "Playfair Display", serif; font-weight: 600;
  }
  .tagline--main { top: 950px; font-size: 38px; line-height: 42px; }
  .tagline--sub { left: 39px; width: auto; top: 1068px; font-size: 20px; text-align: left; letter-spacing: 0.3px; }
</style>
</head>
<body>
  <main class="poster">
    <div class="grill-backdrop" role="img" aria-label="Close-up of a flame-grilled steak over glowing coals"></div>

    <svg class="shade" width="806" height="1136" viewBox="0 0 806 1136" aria-hidden="true">
      <polygon points="443,0 700,0 540,390 300,390" fill="rgba(0,0,0,0.7)"/>
      <polygon points="150,746 430,746 300,1136 0,1136 0,1060" fill="rgba(0,0,0,0.75)"/>
    </svg>

    <div class="photo photo--dining-room" role="img" aria-label="Guests dining in a warmly lit restaurant room"></div>
    <div class="photo photo--toast" role="img" aria-label="Couple toasting with glasses of red wine"></div>

    <div class="brand">Ironfield<br>Grillhouse</div>

    <div class="gold-bar gold-bar--top"></div>
    <div class="headline-veil"></div>
    <div class="gold-bar gold-bar--bottom"></div>

    <h1 class="headline">
      <span class="headline__line headline__line--lead">JUST HAVE TO HAVE AN</span>
      <span class="headline__accent">awesome</span>
      <span class="headline__line headline__line--close">STEAK FOR DINNER</span>
    </h1>

    <p class="tagline tagline--main">People drinking<br>dining</p>
    <p class="tagline tagline--sub">having a great dining experience</p>
  </main>
</body>
</html>
```